Brent's Lot Grading & Trenching

I would like to have business cards created for my land clearing company. We have excavators, skid steers, dump trucks, tractor trailer dump trailers, forestry mulchers along with all size tractors for pasture restoration and arena builds.

Target Market(s)

Both commercial and residential clients

Contact Information for Business Card

Name, phone number, email and website

Colors

Designer to choose colors to be used in the design.

```html
<!DOCTYPE html>
<html lang="en">
<head>
<meta charset="utf-8">
<title>Brent's Lot Grading &amp; Trenching — Business Card</title>
<link rel="stylesheet" href="https://fonts.googleapis.com/css2?family=Oswald:wght@500;600&family=Poppins:wght@400&display=swap">
<style>
  :root {
    --ink: #0b0b0b;
    --shade: #141414;
    --glow: #3a2a14;
    --yellow: #f7c600;
    --white: #ffffff;
    --badge: #e8202a;
  }
  html, body {
    margin: 0;
    padding: 0;
    width: 1200px;
    height: 720px;
    overflow: hidden;
    background: var(--ink);
  }
  .card {
    position: relative;
    width: 1200px;
    height: 720px;
    overflow: hidden;
    background: var(--ink);
    font-family: "Poppins", sans-serif;
    color: var(--white);
  }
  .card__backdrop {
    position: absolute;
    inset: 0;
    background:
      radial-gradient(ellipse 520px 300px at 640px 40px, rgba(120, 80, 30, 0.45), transparent 70%),
      radial-gradient(ellipse 700px 360px at 820px 360px, var(--glow), transparent 75%),
      linear-gradient(180deg, #171310 0%, #0d0c0b 55%, #101010 100%);
  }
  .rule {
    position: absolute;
    left: 0;
    width: 1200px;
    height: 3px;
    background: var(--yellow);
  }
  .rule--top { top: 199px; }
  .rule--bottom { top: 507px; }

  .owner {
    position: absolute;
    left: 91px;
    top: 92px;
  }
  .owner__name {
    margin: 0;
    font-family: "Oswald", sans-serif;
    font-weight: 600;
    font-size: 48px;
    line-height: 1;
    letter-spacing: 1px;
    color: var(--yellow);
  }
  .owner__role {
    margin: 8px 0 0;
    font-size: 21px;
    line-height: 1;
  }

  .brand {
    position: absolute;
    right: 92px;
    top: 100px;
    display: flex;
    align-items: center;
    gap: 18px;
  }
  .brand__name {
    font-family: "Poppins", sans-serif;
    font-weight: 400;
    font-size: 24px;
    line-height: 1.2;
    text-align: right;
    color: var(--white);
  }
  .brand__dot {
    width: 80px;
    height: 80px;
    border-radius: 50%;
    background: var(--yellow);
  }

  .service {
    position: absolute;
    left: 140px;
    width: 920px;
    top: 276px;
    text-align: center;
  }
  .service__title {
    margin: 0;
    font-family: "Oswald", sans-serif;
    font-weight: 600;
    font-size: 37px;
    line-height: 1;
    letter-spacing: 1px;
    color: var(--yellow);
  }
  .service__list {
    margin: 28px 0 0;
    font-size: 22.5px;
    line-height: 32px;
    letter-spacing: 0.3px;
  }

  .contact {
    position: absolute;
    left: 89px;
    top: 524px;
  }
  .contact__phone {
    margin: 0;
    font-family: "Oswald", sans-serif;
    font-weight: 500;
    font-size: 44px;
    line-height: 1;
    letter-spacing: 1.5px;
  }
  .contact__line {
    margin: 0;
    font-size: 21px;
    line-height: 32px;
    letter-spacing: 0.5px;
  }
  .contact__phone + .contact__line { margin-top: 12px; }

  .listings {
    position: absolute;
    left: 962px;
    top: 545px;
    display: flex;
    gap: 12px;
  }
  .listings__badge {
    width: 64px;
    height: 64px;
    border-radius: 50%;
    background: var(--badge);
  }
</style>
</head>
<body>
  <main class="card">
    <div class="card__backdrop" role="img" aria-label="Dark sunset photograph of excavators working on a cleared lot"></div>

    <div class="rule rule--top"></div>
    <div class="rule rule--bottom"></div>

    <header class="owner">
      <h1 class="owner__name">Brent Halvorsen</h1>
      <p class="owner__role">Owner</p>
    </header>

    <div class="brand">
      <div class="brand__name">Brent's Lot Grading<br>&amp; Trenching, LLC</div>
      <div class="brand__dot"></div>
    </div>

    <section class="service">
      <h2 class="service__title">SERVICE AREA:</h2>
      <p class="service__list">Brooksville, Bushnell, Dade City, Land O' Lakes, Lutz, Pasco County, San Antonio, Tampa, Webster, Weeki Wachee Gardens, Wesley Chapel, Zephyrhills</p>
    </section>

    <footer class="contact">
      <p class="contact__phone">813-555-0142</p>
      <p class="contact__line">office@brentslotgrading.com</p>
      <p class="contact__line">www.brentslotgrading.com</p>
    </footer>

    <div class="listings" aria-label="Review listings">
      <span class="listings__badge"></span>
      <span class="listings__badge"></span>
    </div>
  </main>
</body>
</html>
```